Corvant Systems Business Card

Create an appealing and elegant Business card for corvant systems. Include logo and use related colors from website, be creative. Include Business name, my name, tile, address, contacts, address, and social media contacts if possible. Logo PSD file is attached.

Bleed Area: 3.46" x 2.32"
Trim: 3.3" x 2.16"
Safe Area: 3.14" x 2.02"

Save files as vector-based PDF with outlined text and PNG.
No crop marks
CMYK color setting

Business Card Info:

Corvant Systems

Dennis Halvorsen
Owner

512 Brindlemoor Rd Unit C
Harrowgate, EM 02871
t. 1.888.555.0162
e. dennis.h@corvantsys.example
w. www.corvantsys.example

friendloop. www.friendloop.example/CorvantSys
chirpline. chirpline.example/corvantsys
pinboardly. www.pinboardly.example/corvantsys/

Target Market(s)

Business Owners and Partners

Industry/Entity Type

Business

Requirements
Must have
• Logo and related colors from website

```html
<!DOCTYPE html>
<html lang="en">
<head>
<meta charset="utf-8">
<title>Corvant Systems Business Card</title>
<link rel="stylesheet" href="https://fonts.googleapis.com/css2?family=Arimo:wght@400;700&display=swap">
<style>
  :root {
    --page: #e9e6e2;
    --blue-light: #7c9dc6;
    --blue: #6a8dbb;
    --blue-deep: #4e74a8;
    --white: #ffffff;
    --ink: #111111;
    --band-grey: #d3d3d3;
    --title-blue: #4f78ad;
    --black: #050505;
  }
  * { margin: 0; padding: 0; box-sizing: border-box; }
  html, body {
    width: 1200px; height: 914px; overflow: hidden;
    background: var(--page);
    font-family: "Arimo", Arial, sans-serif;
  }
  .canvas { position: relative; width: 1200px; height: 914px; }
  .card {
    position: absolute; left: 290px; width: 620px; height: 406px;
    overflow: hidden;
    box-shadow: 0 6px 18px rgba(0,0,0,.18);
  }
  .card--front { top: 31px; background: linear-gradient(120deg, var(--blue) 0%, var(--blue-light) 45%, var(--blue-deep) 100%); }
  .card--back  { top: 477px; background: linear-gradient(115deg, var(--blue-light) 0%, var(--blue) 50%, var(--blue-deep) 100%); }

  /* front */
  .front__header {
    position: absolute; left: 0; top: 0; width: 620px; height: 150px;
    background: var(--white);
  }
  .front__logo-panel {
    position: absolute; left: 390px; top: 150px; width: 230px; height: 112px;
    background: var(--white);
  }
  .holder { position: absolute; left: 36px; top: 52px; }
  .holder__name { font-size: 27px; color: var(--ink); letter-spacing: .3px; }
  .holder__title { margin-top: 6px; font-size: 17px; color: var(--title-blue); }

  .email-band {
    position: absolute; left: 0; top: 150px; width: 390px; height: 24px;
    background: var(--band-grey);
    font-size: 14px; color: #333; line-height: 24px; padding-left: 50px;
  }
  .brand {
    position: absolute; left: 412px; top: 160px; width: 200px;
    font-weight: 700; color: var(--ink);
    font-size: 36px; line-height: 42px;
  }
  .web-band {
    position: absolute; left: 390px; top: 262px; width: 230px; height: 26px;
    background: var(--black); color: var(--white);
    font-size: 14px; line-height: 26px; text-align: center;
  }
  .contacts {
    position: absolute; left: 30px; top: 196px; width: 350px; list-style: none;
    color: var(--white); font-size: 14px; line-height: 22px;
  }
  .contacts li { display: flex; align-items: center; gap: 10px; white-space: nowrap; }
  .contacts .icon { width: 12px; height: 12px; flex: none; }
  .contacts .no-icon { padding-left: 22px; }

  /* back */
  .back__brand {
    position: absolute; left: 70px; top: 140px;
    font-weight: 700; color: var(--white);
    font-size: 52px; line-height: 58px;
  }
</style>
</head>
<body>
<main class="canvas">
  <section class="card card--front" aria-label="Business card front">
    <div class="front__header"></div>
    <div class="front__logo-panel"></div>

    <div class="holder">
      <p class="holder__name">Dennis Halvorsen</p>
      <p class="holder__title">Owner</p>
    </div>

    <div class="email-band">dennis.h@corvantsys.example</div>

    <p class="brand">Corvant<br>Systems</p>

    <div class="web-band">www.corvantsys.example</div>

    <ul class="contacts">
      <li>
        <svg class="icon" viewBox="0 0 12 12" aria-hidden="true"><path d="M3 1h2l1 3-1.5 1a6 6 0 0 0 2.5 2.5L8 6l3 1v2a2 2 0 0 1-2 2A8 8 0 0 1 1 3a2 2 0 0 1 2-2z" fill="#fff"/></svg>
        1.888.555.0162
      </li>
      <li>
        <svg class="icon" viewBox="0 0 12 12" aria-hidden="true"><circle cx="6" cy="6" r="5.5" fill="#fff"/></svg>
        friendloop. www.friendloop.example/CorvantSys
      </li>
      <li>
        <svg class="icon" viewBox="0 0 12 12" aria-hidden="true"><circle cx="6" cy="6" r="5.5" fill="#fff"/></svg>
        chirpline. chirpline.example/corvantsys
      </li>
      <li>
        <svg class="icon" viewBox="0 0 12 12" aria-hidden="true"><circle cx="6" cy="6" r="5.5" fill="#fff"/></svg>
        pinboardly. www.pinboardly.example/corvantsys/
      </li>
      <li class="no-icon">512 Brindlemoor Rd Unit C Harrowgate, EM 02871</li>
    </ul>
  </section>

  <section class="card card--back" aria-label="Business card back">
    <p class="back__brand">Corvant<br>Systems</p>
  </section>
</main>
</body>
</html>
```